Business card design for new eCommerce site focusing on integrity and strong businsess tactics

We need a business card that will stand out and be memorable. Something with color that matches our company logo colors. Think high end version of Dealvine. There are 2 logos provided. The parent company is called Bright Harbor Ventures and we are presenting a new and very exciting eCommerce site called KeenTraders.example.

Target Market(s)

Our target markets are in the Activities, Food and Beverage, Health and Beauty

Industry/Entity Type

Marketing

Contact Information for Business Card

We have 4 members that need cards...I will provide all info to the winner of the design contest
Business Address is
48730 West 61st Avenue, Suite C204
Phoenix AZ 85917

Font styles to use
Serif
Sans Serif

Colors

Designer to choose colors to be used in the design.

Requirements
Must have
• The card must be memorable...should be unique in design but must exude integrity and be playful .
• I have provided several colors or our parent company...please feel free to use which ever
Nice to have
• I will leave this up to you. Feel free to use other images of your choosing that wraps around our client.....Activities, Dining, Health, Beauty
Should not have
• just dont be boring

```html
<!DOCTYPE html>
<html lang="en">
<head>
<meta charset="utf-8">
<title>Bright Harbor Ventures / KeenTraders.example business card</title>
<link rel="stylesheet" href="https://fonts.googleapis.com/css2?family=Roboto:wght@400;500;700&display=swap">
<style>
  :root {
    --backdrop: #e8e8e8;
    --navy-deep: #101a48;
    --navy-light: #1f2a5c;
    --white: #ffffff;
    --green: #7dc243;
    --blue: #2f7fb8;
    --grey-text: #6b6b6b;
    --card-shadow: rgba(0, 0, 0, 0.28);
  }
  html, body {
    margin: 0;
    padding: 0;
    width: 1200px;
    height: 1000px;
    overflow: hidden;
    background: var(--backdrop);
    font-family: "Roboto", Arial, sans-serif;
  }
  .canvas {
    position: relative;
    width: 1200px;
    height: 1000px;
  }
  .card {
    position: absolute;
    left: 269px;
    width: 662px;
    height: 378px;
    border-radius: 20px;
    overflow: hidden;
    box-shadow: 0 4px 8px var(--card-shadow);
  }

  /* Front side */
  .card--front {
    top: 108px;
    background: linear-gradient(120deg, var(--navy-deep) 0%, var(--navy-deep) 45%, var(--navy-light) 100%);
  }
  .brand-mark {
    position: absolute;
    left: 263px;
    top: 94px;
    width: 136px;
    height: 136px;
    border-radius: 50%;
    background: var(--white);
  }
  .brand-name {
    position: absolute;
    left: 0;
    right: 0;
    top: 236px;
    text-align: center;
    color: var(--white);
    font-size: 33px;
    font-weight: 700;
    letter-spacing: 0.2px;
  }

  /* Back side */
  .card--back {
    top: 520px;
    height: 380px;
    background: var(--white);
  }
  .site-mark {
    position: absolute;
    left: 52px;
    top: 58px;
    width: 62px;
    height: 62px;
    border-radius: 50%;
    background: var(--green);
  }
  .site-name {
    position: absolute;
    left: 130px;
    top: 66px;
    color: var(--green);
    font-size: 30px;
    font-weight: 500;
    letter-spacing: -0.3px;
  }
  .site-tagline {
    position: absolute;
    left: 131px;
    top: 106px;
    color: var(--blue);
    font-size: 14px;
    letter-spacing: 1.4px;
  }
  .contact {
    position: absolute;
    left: 129px;
    top: 188px;
    color: var(--grey-text);
    font-size: 15px;
    line-height: 19px;
  }
  .contact__name {
    font-size: 19px;
    font-weight: 700;
    line-height: 24px;
  }
  .contact__first { color: var(--green); }
  .contact__last { color: var(--blue); }
  .contact__title { margin-bottom: 12px; }
  .contact__address { margin-bottom: 15px; }
  .contact__line {
    display: flex;
    align-items: center;
    gap: 4px;
    margin-bottom: 6px;
  }
  .contact__line svg {
    width: 12px;
    height: 12px;
    fill: var(--blue);
  }
  .card-stripe--green {
    position: absolute;
    left: 0;
    right: 0;
    bottom: 12px;
    height: 3px;
    background: var(--green);
  }
  .card-stripe--blue {
    position: absolute;
    left: 0;
    right: 0;
    bottom: 0;
    height: 10px;
    background: var(--blue);
  }
</style>
</head>
<body>
<main class="canvas">

  <section class="card card--front" aria-label="Card front">
    <div class="brand-mark"></div>
    <div class="brand-name">Bright Harbor Ventures</div>
  </section>

  <section class="card card--back" aria-label="Card back">
    <div class="site-mark"></div>
    <div class="site-name">KeenTraders.example</div>
    <div class="site-tagline">Activities-Dining-Health-Beauty</div>

    <div class="contact">
      <div class="contact__name"><span class="contact__first">Owen</span> <span class="contact__last">Hartley</span></div>
      <div class="contact__title">Managing Director</div>
      <div class="contact__address">48730 West 61st Avenue, Suite C204<br>Phoenix AZ 85917</div>
      <div class="contact__line">
        <svg viewBox="0 0 24 24" aria-hidden="true"><path d="M6.6 10.8c1.4 2.8 3.8 5.1 6.6 6.6l2.2-2.2c.3-.3.7-.4 1-.2 1.1.4 2.3.6 3.6.6.6 0 1 .4 1 1V20c0 .6-.4 1-1 1C10.6 21 3 13.4 3 4c0-.6.4-1 1-1h3.5c.6 0 1 .4 1 1 0 1.3.2 2.5.6 3.6.1.3 0 .7-.2 1z"/></svg>
        <span>+61 400 555 019</span>
      </div>
      <div class="contact__line">
        <svg viewBox="0 0 24 24" aria-hidden="true"><path d="M2 5h20v14H2z M2 5l10 8 10-8" stroke="#fff" stroke-width="1.5"/></svg>
        <span>info@KeenTraders.example</span>
      </div>
    </div>

    <div class="card-stripe--green"></div>
    <div class="card-stripe--blue"></div>
  </section>

</main>
</body>
</html>
```